Advertisement for a Digital Strategy Consultancy

We are 'PELICORN BRAANDA' a boutique agency that focuses on Digital Strategies for business. (i.e. online branding, social publicity stunts, viral advertising etc etc..)

We need a 30 second advertisement for the agency that says...

Holy crap dude... They look like they know what they are doing. Very simple and minimal tho...

Here is some inspiration:

http://portal.quilvanto.example/app/FullPlayer.aspx?id=a482917e-3b0c-472d-9e1f-77cbd0a3f109

Reason: We advertised the project as an advertisement when we are really chasing more of an animated slideshow

Reason: The project requires some planning that we feel justifies the amendment to the deadline.

Target Market(s)

Our target demographic is the typical 40+ year old that knows that in this day and age, he/she really should be putting more effort into the companies online marketing and advertising campaigns. BUT... Unfortunately for the company, somewhere along the way this person has like so many others, been convinced that instead of learning about what they are doing themselves, they should just pay some cheesy old man in a tracksuit to create them an bidlists campaign.

Industry/Entity Type

Advertising

Requirements
Must have
• Our url will be:

www.pelicornbraanda.example

The add must simply show the domain address somewhere/how?

Nice to have
• A high res version and a web optimised low res version of the ad
Should not have
• stolen ideas

```html
<!DOCTYPE html>
<html lang="en">
<head>
<meta charset="utf-8">
<title>PELICORN BRAANDA — Have? Confused?</title>
<link rel="stylesheet" href="https://fonts.googleapis.com/css2?family=Open+Sans:wght@600;700&display=swap">
<style>
  :root {
    --bg-center: #ffffff;
    --bg-edge: #b9c8d3;
    --ink-brown: #4a1f00;
    --accent-orange: #fbb93a;
    --accent-yellow: #f2e24f;
    --bar-black: #000000;
    --band-top: #474c54;
    --band-bottom: #000000;
    --bubble-core: #fff24f;
    --bubble-edge: #fbbd37;
    --caption-light: #f2f2f2;
    --caption-shade: #bfbfbf;
  }
  * { margin: 0; padding: 0; box-sizing: border-box; }
  html, body { width: 1200px; height: 900px; overflow: hidden; background: var(--bg-edge); }
  .slide {
    position: relative;
    width: 1200px;
    height: 900px;
    overflow: hidden;
    background: radial-gradient(ellipse 720px 620px at 630px 320px, var(--bg-center) 0%, #e4eaee 35%, var(--bg-edge) 100%);
    font-family: "Open Sans", "Segoe UI", sans-serif;
  }
  .top-rule { position: absolute; top: 32px; height: 33px; }
  .top-rule--accent { left: 723px; width: 70px; background: var(--accent-orange); }
  .top-rule--bar { left: 793px; width: 407px; background: var(--bar-black); }
  .bubble {
    position: absolute;
    border-radius: 50%;
    background: radial-gradient(circle at 50% 50%, var(--bubble-core) 0%, #fdd842 45%, var(--bubble-edge) 100%);
  }
  .bubble--have { left: 361px; top: 65px; width: 276px; height: 276px; }
  .bubble--confused { left: 813px; top: 295px; width: 342px; height: 342px; }
  .word {
    position: absolute;
    color: var(--ink-brown);
    font-weight: 700;
    line-height: 1;
    white-space: nowrap;
  }
  .word--have { left: 78px; top: 99px; font-size: 166px; letter-spacing: -6px; }
  .word--confused { left: 214px; top: 378px; font-size: 164px; letter-spacing: -4px; }
  .mark {
    position: absolute;
    color: var(--ink-brown);
    font-weight: 700;
    line-height: 1;
  }
  .mark--have { left: 452px; top: 71px; font-size: 233px; }
  .mark--confused { left: 936px; top: 316px; font-size: 270px; }
  .caption-band {
    position: absolute;
    left: 0; top: 672px;
    width: 1113px; height: 169px;
    background: linear-gradient(180deg, var(--band-top) 0%, #1c1e21 55%, var(--band-bottom) 100%);
  }
  .caption-tab {
    position: absolute;
    left: 1116px; top: 672px;
    width: 54px; height: 169px;
    background: linear-gradient(180deg, var(--accent-yellow) 0%, var(--accent-orange) 100%);
  }
  .caption {
    position: absolute;
    right: 116px; top: 696px;
    font-size: 88px;
    font-weight: 600;
    line-height: 1.2;
    white-space: nowrap;
    letter-spacing: -1.2px;
    background: linear-gradient(180deg, var(--caption-light) 30%, var(--caption-shade) 100%);
    -webkit-background-clip: text;
    background-clip: text;
    color: transparent;
  }
</style>
</head>
<body>
  <main class="slide">
    <div class="top-rule top-rule--accent"></div>
    <div class="top-rule top-rule--bar"></div>

    <div class="bubble bubble--have"></div>
    <div class="bubble bubble--confused"></div>

    <h1 class="word word--have">Have</h1>
    <span class="mark mark--have">?</span>

    <h2 class="word word--confused">Confused</h2>
    <span class="mark mark--confused">?</span>

    <div class="caption-band"></div>
    <div class="caption-tab"></div>
    <p class="caption">Want to Get it right!!!</p>
  </main>
</body>
</html>
```